Luxury Toilet Rental Business. Quellwick Hire.

Quellwick Hire (the logo is in the uploaded files)
We RENT and SELL Luxury Trailer toilets.
- Show location, number, pricing, pictures.
- We have two stall trailers for rent AND 3 stall trailers
- We sell them too
- We want our phone number shown
- We are a local company
- Slogan: Brighten your gathering with Quellwick Hire. The Opulent Washroom
- We want a pricing portion
- We want the sizes shown
- We want the different rates/ prices shown
- We do 1 day rentals
- We do 1 week rentals
- We want the service area. We serve Los Angeles County, Orange County, Riverside County, San Bernardino County, and Palm Desert.
- Our location is in Santa Ana California

Target Market(s)

Event planners, wedding planners, venue planners, concerts, events, gatherings.

Industry/Entity Type

Luxury Toilet Rentals

Number of Pages Required

1 page

Font styles to use
Serif
Sans Serif

Colors
EE7325
F08F49
F5BC92
FAE3D3
FDF4ED

Requirements
Must have
• Location, pricing, pictures, available areas. Our slogan.
Nice to have
• I like the idea of having tabs that show price, a tab that shows our contact information, pictures, event ideas, and where we service (the areas we'll go to)

```html
<!DOCTYPE html>
<html lang="en">
<head>
<meta charset="utf-8">
<title>Quellwick Hire — Luxury Trailer Toilet Rentals</title>
<link href="https://fonts.googleapis.com/css2?family=Montserrat:wght@500;600;700;800&family=Roboto:wght@400;500;700&display=swap" rel="stylesheet">
<style>
:root{
  --orange:#ee7325;
  --orange-mid:#f08f49;
  --orange-soft:#f5bc92;
  --orange-pale:#fae3d3;
  --cream:#fdf4ed;
  --slate:#58585a;
  --ink:#474747;
  --text:#3c3c3c;
  --muted:#6a6a6a;
  --grey-bg:#eeeeee;
  --footer:#0b0b0b;
  --white:#ffffff;
}
*{box-sizing:border-box;margin:0;padding:0}
html,body{width:1200px;height:4732px;overflow:hidden}
body{position:relative;background:var(--white);font-family:"Roboto",Arial,sans-serif;color:var(--text)}
.abs{position:absolute}
.head-font{font-family:"Montserrat",Arial,sans-serif}
.photo{position:absolute;display:block}
.btn{position:absolute;display:flex;align-items:center;justify-content:center;font-family:"Montserrat",Arial,sans-serif;font-weight:700;font-size:13px;letter-spacing:.3px;border-radius:3px}
.btn-solid{background:var(--orange);color:var(--white)}
.btn-line{border:1.5px solid var(--orange);color:var(--orange);background:var(--white)}
.section-title{position:absolute;left:0;width:1200px;text-align:center;font-family:"Montserrat",Arial,sans-serif;font-weight:800;font-size:34px;letter-spacing:.5px}
.section-title span{color:var(--orange)}

/* header */
.brand{position:absolute;left:190px;top:26px;width:226px;height:44px;display:flex;align-items:center;justify-content:center;font-family:"Montserrat",Arial,sans-serif;font-weight:800;font-size:27px;color:var(--orange);letter-spacing:.5px}
.head-contact{position:absolute;top:26px;display:flex;gap:12px;align-items:flex-start}
.head-contact .label{font-family:"Montserrat",Arial,sans-serif;font-weight:700;font-size:15px;color:var(--orange)}
.head-contact .value{font-size:13.5px;color:var(--text);margin-top:3px}
.nav{position:absolute;top:92px;left:0;width:1200px;height:51px;background:var(--slate)}
.nav a{position:absolute;top:0;height:51px;line-height:51px;color:var(--white);font-size:13.5px;text-decoration:none;transform:translateX(-50%);white-space:nowrap}
.nav a.active{background:var(--orange);width:84px;text-align:center}

/* hero */
.hero{position:absolute;top:143px;left:0;width:1200px;height:599px;overflow:hidden}
.hero h1{position:absolute;left:60px;top:112px;font-family:"Montserrat",Arial,sans-serif;font-weight:800;font-size:38px;line-height:50px;color:var(--white);letter-spacing:.5px}
.hero p{position:absolute;left:60px;top:270px;width:390px;font-size:14px;line-height:24px;color:var(--white)}
.dot{position:absolute;top:489px;width:11px;height:11px;border-radius:50%}

/* cards */
.card{position:absolute;background:var(--white);box-shadow:0 2px 12px rgba(0,0,0,.14)}
.prod-title{position:absolute;left:0;width:100%;text-align:center;font-family:"Montserrat",Arial,sans-serif;font-weight:700;font-size:18px;line-height:24px;color:var(--orange)}
.prod-text{position:absolute;left:30px;right:30px;text-align:center;font-size:14px;line-height:22px;color:var(--text)}

/* about */
.about-text{position:absolute;left:609px;width:455px;font-size:13.5px;line-height:24.5px;color:var(--muted)}

/* service */
.svc-card{position:absolute;top:2236px;width:229px;height:226px;background:var(--white);border-radius:6px;overflow:hidden}
.svc-card .photo{left:4px;top:4px;width:221px;height:176px;border-radius:4px}
.svc-card .label{position:absolute;left:0;bottom:14px;width:100%;text-align:center;font-family:"Montserrat",Arial,sans-serif;font-weight:500;font-size:15px;color:var(--text)}

/* pricing */
.price-title{position:absolute;left:0;width:100%;text-align:center;font-family:"Montserrat",Arial,sans-serif;font-weight:600;font-size:15px;color:var(--text)}
.price-amount{position:absolute;left:0;width:100%;text-align:center;font-family:"Montserrat",Arial,sans-serif;font-weight:700;font-size:25px;color:var(--orange)}
.price-text{position:absolute;left:40px;right:40px;text-align:center;font-size:11px;line-height:17px;color:var(--text)}

/* areas */
.area .photo{top:3268px;width:194px;height:192px}
.area-label{position:absolute;top:3470px;width:194px;text-align:center;font-family:"Montserrat",Arial,sans-serif;font-weight:500;font-size:19px;color:var(--white)}

/* contact */
.field{position:absolute;border:1.5px solid #555;border-radius:4px;background:var(--white);display:flex;align-items:center;gap:8px;padding-left:18px;font-size:12px;color:#444}
.field.message{align-items:flex-start;padding-top:16px}
.info-row{position:absolute;left:145px;display:flex;align-items:flex-start;gap:14px;font-size:15px;line-height:23px;color:var(--text)}
.info-icon{width:36px;height:36px;border-radius:50%;background:#e2e2e2;display:flex;align-items:center;justify-content:center;flex-shrink:0}

/* footer */
.footer{position:absolute;top:4241px;left:0;width:1200px;height:491px;background:var(--footer);color:var(--white)}
.foot-head{position:absolute;top:96px;font-family:"Montserrat",Arial,sans-serif;font-weight:700;font-size:15px;letter-spacing:.5px}
.foot-list{position:absolute;list-style:none;font-size:13.5px}
.foot-list li{height:29.6px;display:flex;align-items:center;gap:8px}
.foot-contact{position:absolute;left:322px;font-size:14px;line-height:22px;display:flex;gap:8px}
.social{position:absolute;left:586px;display:flex;align-items:center;gap:12px;font-size:15px}
.social i{width:28px;height:28px;border-radius:50%;background:#d9d9d9;display:block}
</style>
</head>
<body>

<!-- Header -->
<header>
  <div class="brand">Quellwick Hire</div>
  <div class="head-contact" style="left:510px">
    <svg width="40" height="40" viewBox="0 0 40 40" aria-hidden="true"><rect x="3" y="12" width="34" height="24" rx="2" fill="none" stroke="var(--orange)" stroke-width="3"/><path d="M3 14 L20 27 L37 14" fill="none" stroke="var(--orange)" stroke-width="3"/><circle cx="20" cy="9" r="7" fill="var(--orange)"/></svg>
    <div><div class="label">Email Us :</div><div class="value">info@quellwickhire.com</div></div>
  </div>
  <div class="head-contact" style="left:743px">
    <svg width="42" height="42" viewBox="0 0 42 42" aria-hidden="true"><circle cx="21" cy="21" r="18" fill="none" stroke="var(--orange)" stroke-width="3"/><path d="M14 12c2 0 3 4 2 5l-2 2c1 3 4 6 7 7l2-2c1-1 5 0 5 2l-1 3c-1 2-4 2-8 0-4-2-8-6-9-10-1-3 0-6 2-7z" fill="var(--orange)"/></svg>
    <div><div class="label">Phone Number :</div><div class="value">+1 555 014 2290</div></div>
  </div>
</header>

<nav class="nav">
  <a class="active" style="left:207px">Home</a>
  <a style="left:303px">About Us</a>
  <a style="left:438px">Where We Service</a>
  <a style="left:585px">Service area</a>
  <a style="left:695px">Pricing</a>
  <a style="left:787px">Gallery</a>
  <a style="left:875px">Event</a>
  <a style="left:977px">Contact Us</a>
</nav>

<!-- Hero -->
<section class="hero">
  <svg class="photo" width="1200" height="599" role="img" aria-label="Grey three-stall luxury toilet trailer with metal steps parked on a concrete lot">
    <defs><linearGradient id="heroPhoto" x1="0" y1="0" x2="0" y2="1"><stop offset="0" stop-color="#b9bcc0"/><stop offset=".45" stop-color="#77797c"/><stop offset="1" stop-color="#a6a6a4"/></linearGradient></defs>
    <rect width="1200" height="599" fill="url(#heroPhoto)"/>
  </svg>
  <svg class="photo" width="1200" height="599" aria-hidden="true">
    <defs><linearGradient id="heroOrange" x1="0" y1="0" x2="1" y2="0"><stop offset="0" stop-color="#ec6f2a"/><stop offset="1" stop-color="var(--orange-mid)"/></linearGradient></defs>
    <polygon points="0,0 612,0 455,599 0,599" fill="url(#heroOrange)"/>
  </svg>
  <h1>WELCOME TO<br>QUELLWICK HIRE<br>LOCAL COMPANY</h1>
  <p>Brighten your gathering with Quellwick Hire. The Opulent Washroom, delivered from Santa Ana for one day or a full week.</p>
  <div class="btn" style="left:60px;top:369px;width:128px;height:40px;background:var(--white);color:var(--orange)">DAY RENTALS</div>
  <div class="btn" style="left:200px;top:369px;width:142px;height:40px;border:2px solid var(--white);color:var(--white)">WEEK RENTALS</div>
  <span class="dot" style="left:63px;border:2px solid var(--white)"></span>
  <span class="dot" style="left:86px;background:var(--white)"></span>
  <span class="dot" style="left:108px;background:var(--white)"></span>
</section>

<!-- Products -->
<section>
  <h2 class="section-title" style="top:814px;color:var(--ink)">OUR <span>PRODUCTS</span></h2>

  <div class="card" style="left:202px;top:900px;width:380px;height:505px">
    <svg class="photo" style="left:8px;top:10px" width="364" height="258" role="img" aria-label="Two stall toilet trailer parked outside a warehouse"><rect width="364" height="258" fill="#8f9296"/><rect y="150" width="364" height="108" fill="#a9a9a7"/></svg>
    <div class="prod-title" style="top:290px">TWO STALL TRAILERS<br>TALILER : 7'X 8'</div>
    <p class="prod-text" style="top:350px">Two private stalls with sinks, mirrors and soft lighting. Ideal for weddings, parties and smaller events.</p>
    <div class="btn btn-solid" style="left:96px;top:432px;width:97px;height:40px">SELL</div>
    <div class="btn btn-line" style="left:200px;top:432px;width:88px;height:40px">RENT</div>
  </div>

  <div class="card" style="left:618px;top:900px;width:380px;height:505px">
    <svg class="photo" style="left:8px;top:10px" width="364" height="258" role="img" aria-label="Three stall toilet trailer with blue steps parked outside a warehouse"><rect width="364" height="258" fill="#8f9296"/><rect y="150" width="364" height="108" fill="#a9a9a7"/><rect x="70" y="190" width="200" height="22" fill="#3b8fb5"/></svg>
    <div class="prod-title" style="top:294px">3 STALL TRAILERS<br>TALILER : 7'X 14'</div>
    <p class="prod-text" style="top:348px">Three climate controlled stalls for larger crowds at concerts, venues and festivals across the region.</p>
    <div class="btn btn-solid" style="left:96px;top:430px;width:97px;height:40px">SELL</div>
    <div class="btn btn-line" style="left:200px;top:430px;width:88px;height:40px">RENT</div>
  </div>
</section>

<!-- About -->
<section class="abs" style="left:0;top:1485px;width:1200px;height:597px;background:var(--grey-bg)">
  <svg class="photo" width="1200" height="597" aria-hidden="true">
    <path d="M136 345 V97 H399 V107" fill="none" stroke="var(--orange)" stroke-width="3"/>
    <path d="M537 115 H552 V503 H537" fill="none" stroke="var(--slate)" stroke-width="3"/>
  </svg>
  <svg class="photo" style="left:150px;top:115px" width="387" height="388" role="img" aria-label="Single luxury toilet trailer in front of a building, video preview"><rect width="387" height="388" fill="#9a9c9e"/><rect y="230" width="387" height="158" fill="#b1b0ae"/><circle cx="193" cy="193" r="28" fill="#e2231a"/><polygon points="184,180 206,193 184,206" fill="#fff"/></svg>
  <h2 class="abs head-font" style="left:609px;top:107px;font-weight:800;font-size:34px;color:var(--ink)">ABOUT <span style="color:var(--orange)">US</span></h2>
  <p class="about-text" style="top:168px">Quellwick Hire is a local, family run company based in Santa Ana, California. We rent and sell luxury trailer toilets that bring comfort and style to every guest, from backyard weddings to large outdoor concerts.</p>
  <p class="about-text" style="top:276px">Every trailer is cleaned, stocked and inspected before it leaves our yard. Choose a two stall 7' x 8' trailer or a three stall 7' x 14' trailer, book it for a single day or a full week, and we handle delivery, setup and pickup. We serve Los Angeles County, Orange County, Riverside County, San Bernardino County and Palm Desert, and we work closely with event, wedding and venue planners.</p>
  <div class="btn btn-solid" style="left:609px;top:443px;width:138px;height:39px">READ MORE</div>
</section>

<!-- Where we service -->
<section class="abs" style="left:0;top:2082px;width:1200px;height:481px;overflow:hidden">
  <svg class="photo" width="1200" height="481" role="img" aria-label="Orange-toned backdrop of a toilet trailer"><defs><linearGradient id="svcBg" x1="0" y1="0" x2="1" y2="1"><stop offset="0" stop-color="#ea6f2c"/><stop offset=".5" stop-color="var(--orange-mid)"/><stop offset="1" stop-color="#e0692a"/></linearGradient></defs><rect width="1200" height="481" fill="url(#svcBg)"/></svg>
  <h2 class="section-title" style="top:60px;color:var(--white)">WHERE WE SERVICE</h2>
</section>
<div class="svc-card" style="left:119px"><svg class="photo" role="img" aria-label="Construction site with cranes and scaffolding"><rect width="221" height="176" fill="#7d9fc4"/></svg><div class="label">Construction</div></div>
<div class="svc-card" style="left:362px"><svg class="photo" role="img" aria-label="Outdoor wedding reception under string lights at dusk"><rect width="221" height="176" fill="#6a4a2a"/></svg><div class="label">Outdoor Weddings</div></div>
<div class="svc-card" style="left:607px"><svg class="photo" role="img" aria-label="Cheering crowd at a sports event"><rect width="221" height="176" fill="#7a5a3a"/></svg><div class="label">Sport Events</div></div>
<div class="svc-card" style="left:851px"><svg class="photo" role="img" aria-label="Outdoor event crowd in a park at sunset"><rect width="221" height="176" fill="#8a6a34"/></svg><div class="label">Outdoor Events</div></div>

<!-- Pricing -->
<section>
  <h2 class="abs head-font" style="left:103px;top:2726px;font-weight:800;font-size:36px;color:var(--ink)">OUR <span style="color:var(--orange)">PRICING</span></h2>
  <p class="abs" style="left:103px;top:2780px;width:365px;font-size:13px;line-height:24px;color:var(--text)">Rent either trailer by the day or by the week, or buy one outright. Delivery, setup and pickup from our Santa Ana yard are included.</p>
  <div class="btn btn-solid" style="left:105px;top:2868px;width:97px;height:38px">SELL</div>
  <div class="btn btn-line" style="left:207px;top:2868px;width:88px;height:38px">RENT</div>

  <div class="card" style="left:507px;top:2625px;width:299px;height:395px">
    <svg class="photo" style="left:7px;top:7px" width="286" height="173" role="img" aria-label="Two stall toilet trailer outside a building"><rect width="286" height="173" fill="#8f9296"/><rect y="105" width="286" height="68" fill="#a9a9a7"/></svg>
    <div class="price-title" style="top:212px">2 Stall Trailers Taliler : 7'x 8'</div>
    <div class="price-amount" style="top:242px">$85.00</div>
    <p class="price-text" style="top:285px">Per day rental. Week rates and purchase pricing available on request.</p>
    <div class="btn btn-solid" style="left:115px;top:327px;width:78px;height:30px;font-size:11px">SELL</div>
  </div>

  <div class="card" style="left:827px;top:2625px;width:298px;height:395px">
    <svg class="photo" style="left:7px;top:7px" width="285" height="173" role="img" aria-label="Three stall toilet trailer with blue steps"><rect width="285" height="173" fill="#8f9296"/><rect y="105" width="285" height="68" fill="#a9a9a7"/><rect x="70" y="120" width="140" height="14" fill="#3b8fb5"/></svg>
    <div class="price-title" style="top:210px">3 Stall Trailers Taliler : 7'x 14'</div>
    <div class="price-amount" style="top:240px">$185.00</div>
    <p class="price-text" style="top:283px">Per day rental. Week rates and purchase pricing available on request.</p>
    <div class="btn btn-solid" style="left:115px;top:325px;width:78px;height:30px;font-size:11px">SELL</div>
  </div>
</section>

<!-- Areas -->
<section class="area">
  <div class="abs" style="left:0;top:3106px;width:1200px;height:511px;background:var(--slate)"></div>
  <h2 class="section-title" style="top:3186px;color:var(--white)">AREAS WE SERVE</h2>
  <svg class="photo" style="left:95px" width="194" height="192" role="img" aria-label="Los Angeles skyline at dusk"><rect width="194" height="192" fill="#6b4a3c"/></svg>
  <svg class="photo" style="left:298px" width="194" height="192" role="img" aria-label="Orange County beach pier with palm trees"><rect width="194" height="192" fill="#c9b48e"/></svg>
  <svg class="photo" style="left:503px" width="194" height="192" role="img" aria-label="Riverside County city towers under blue sky"><rect width="194" height="192" fill="#7ea6c9"/></svg>
  <svg class="photo" style="left:708px" width="194" height="192" role="img" aria-label="Palm Desert palms reflected in a lake"><rect width="194" height="192" fill="#4f7fa8"/></svg>
  <svg class="photo" style="left:912px" width="194" height="192" role="img" aria-label="San Bernardino valley with mountains"><rect width="194" height="192" fill="#8a9aa6"/></svg>
  <div class="area-label" style="left:95px">Los Angeles</div>
  <div class="area-label" style="left:298px">Orange County</div>
  <div class="area-label" style="left:503px">Riverside County</div>
  <div class="area-label" style="left:708px">Palm Desert</div>
  <div class="area-label" style="left:912px">San Bernardino</div>
</section>

<!-- Contact -->
<section class="abs" style="left:0;top:3617px;width:1200px;height:624px;background:#f4f4f4;overflow:hidden">
  <svg class="photo" style="left:0;top:420px" width="1200" height="204" role="img" aria-label="Faint city skyline with palm trees"><defs><linearGradient id="skyline" x1="0" y1="0" x2="0" y2="1"><stop offset="0" stop-color="#f4f4f4"/><stop offset="1" stop-color="#d6d6d6"/></linearGradient></defs><rect width="1200" height="204" fill="url(#skyline)"/></svg>
  <h2 class="section-title" style="top:79px;color:#6b6b6b">CONTACT <span>US</span></h2>
  <div class="abs head-font" style="left:145px;top:165px;font-weight:700;font-size:19px;line-height:24px;color:var(--text)">Let's Make&nbsp; Something<br>great Together</div>
  <p class="abs" style="left:145px;top:231px;width:340px;font-size:17px;line-height:24px;color:var(--text)">Tell us your date and guest count and we will reply within a day</p>
</section>
<div class="info-row" style="top:3917px"><span class="info-icon"><svg width="14" height="18" viewBox="0 0 14 18"><path d="M7 0C3 0 0 3 0 7c0 5 7 11 7 11s7-6 7-11C14 3 11 0 7 0z" fill="#222"/><circle cx="7" cy="7" r="2.5" fill="#e2e2e2"/></svg></span><span style="font-size:14px">1200 Harbor Way, Santa Ana<br>California 92701</span></div>
<div class="info-row" style="top:3987px"><span class="info-icon"><svg width="15" height="15" viewBox="0 0 15 15"><path d="M3 0c1.5 0 2.5 3 1.5 4l-1 1c1 2.5 3 4.5 5.5 5.5l1-1c1-1 4 0 4 1.5l-.5 2c-.7 1.5-3 1.5-6 0C4.5 11.5 2 9 1 6 .3 3.5.8 1 3 0z" fill="#222"/></svg></span><span style="font-size:14px;line-height:36px">+1 555 014 2290</span></div>
<div class="info-row" style="top:4045px"><span class="info-icon"><svg width="16" height="12" viewBox="0 0 16 12"><rect x="1" y="1" width="14" height="10" fill="none" stroke="#222" stroke-width="1.6"/><path d="M1 1l7 6 7-6" fill="none" stroke="#222" stroke-width="1.6"/></svg></span><span style="line-height:36px">info@quellwickhire.com</span></div>

<div class="field" style="left:532px;top:3775px;width:252px;height:45px"><svg width="10" height="11" viewBox="0 0 10 11"><circle cx="5" cy="3" r="3" fill="#333"/><path d="M0 11c0-4 10-4 10 0z" fill="#333"/></svg>First Name</div>
<div class="field" style="left:805px;top:3775px;width:253px;height:45px"><svg width="10" height="11" viewBox="0 0 10 11"><circle cx="5" cy="3" r="3" fill="#333"/><path d="M0 11c0-4 10-4 10 0z" fill="#333"/></svg>Last Name</div>
<div class="field" style="left:532px;top:3843px;width:252px;height:45px"><svg width="12" height="9" viewBox="0 0 12 9"><rect x=".7" y=".7" width="10.6" height="7.6" fill="none" stroke="#333" stroke-width="1.3"/><path d="M1 1l5 4 5-4" fill="none" stroke="#333" stroke-width="1.3"/></svg>Email</div>
<div class="field" style="left:805px;top:3843px;width:253px;height:45px"><svg width="11" height="11" viewBox="0 0 15 15"><path d="M3 0c1.5 0 2.5 3 1.5 4l-1 1c1 2.5 3 4.5 5.5 5.5l1-1c1-1 4 0 4 1.5l-.5 2c-.7 1.5-3 1.5-6 0C4.5 11.5 2 9 1 6 .3 3.5.8 1 3 0z" fill="#333"/></svg>Phone</div>
<div class="field message" style="left:532px;top:3912px;width:526px;height:140px"><svg width="12" height="9" viewBox="0 0 12 9"><rect x=".7" y=".7" width="10.6" height="7.6" fill="none" stroke="#333" stroke-width="1.3"/><path d="M1 1l5 4 5-4" fill="none" stroke="#333" stroke-width="1.3"/></svg>Message</div>
<div class="btn btn-solid" style="left:533px;top:4062px;width:114px;height:38px">SUBMIT</div>

<!-- Footer -->
<footer class="footer">
  <div class="foot-head" style="left:124px">QUICK LINKS</div>
  <ul class="foot-list" style="left:124px;top:127px">
    <li>&raquo; Home</li><li>&raquo; About Us</li><li>&raquo; Where We Service</li><li>&raquo; Service area</li><li>&raquo; Pricing</li><li>&raquo; Gallery</li><li>&raquo; Event</li><li>&raquo; Contact Us</li>
  </ul>

  <div class="foot-head" style="left:322px;top:100px">CONTACT INFO</div>
  <div class="foot-contact" style="top:135px"><svg width="10" height="14" viewBox="0 0 14 18" style="margin-top:4px"><path d="M7 0C3 0 0 3 0 7c0 5 7 11 7 11s7-6 7-11C14 3 11 0 7 0z" fill="#fff"/></svg><span>1200 Harbor Way, Santa Ana<br>California 92701</span></div>
  <div class="foot-contact" style="top:186px"><svg width="11" height="11" viewBox="0 0 15 15" style="margin-top:5px"><path d="M3 0c1.5 0 2.5 3 1.5 4l-1 1c1 2.5 3 4.5 5.5 5.5l1-1c1-1 4 0 4 1.5l-.5 2c-.7 1.5-3 1.5-6 0C4.5 11.5 2 9 1 6 .3 3.5.8 1 3 0z" fill="#fff"/></svg><span>+1 555 014 2290</span></div>
  <div class="foot-contact" style="top:219px"><svg width="12" height="9" viewBox="0 0 12 9" style="margin-top:7px"><rect width="12" height="9" fill="#fff"/><path d="M0 0l6 5 6-5" fill="none" stroke="#0b0b0b" stroke-width="1.3"/></svg><span>info@quellwickhire.com</span></div>

  <div class="foot-head" style="left:586px">FOLLOW US</div>
  <div class="social" style="top:130px"><i></i>Friendsfeed</div>
  <div class="social" style="top:172px"><i></i>Chirpline</div>
  <div class="social" style="top:212px"><i></i>Worklink</div>
  <div class="social" style="top:254px"><i></i>Pinboard</div>

  <div class="abs head-font" style="left:772px;top:114px;width:303px;height:66px;display:flex;align-items:center;justify-content:center;font-weight:800;font-size:30px;color:var(--orange)">Quellwick Hire</div>

  <div class="abs" style="left:105px;top:407px;width:990px;height:1px;background:#2a2a2a"></div>
  <div class="abs" style="left:0;top:442px;width:1200px;text-align:center;font-size:13px;color:#e6e6e6">&copy; 2024&nbsp; Quellwick Hire | All Rights Reserved</div>
</footer>

</body>
</html>
```